'Ormel Property Development' Business Card

Business Card Features:

High Quality (potentially textured) thick card - preference is white textured card

Logo (supplied)

We plan to use the vertical logo as the main logo. But i am happy for people to use either if they find it works better for the design of the card.

The building icon and also the insert to the 'E' is in a metallic finish, i think this should be finished in a metallic embossed or raised style.
Updates

Please note i have attached both a horizontal and Vertical Logo for your reference. We plan to use the vertical logo as the main logo. But i am happy for people to use either if they find it works better for the design of the card.

Please note i am considering having the cards made on stainless steel. This introduces the option of having cut outs in the card and etching or printing for the design. If you have a good concept for this please submit.

http://www.tinquarry.example/black-metal-cards# this is a site that makes the metal cards to offer some direction . . . . Please note i am basic the selection o the best design, if that means normal print cards on paper then this is what i will choose. But there are some great options with the metal. Thanks.

Industry/Entity Type

Building

Requirements
Must have
• Helvetica font to details side of card - logo as supplied to opposite side.

Card Details:

Darrow Pketts
Managing Director

+61 487 263 518
+61 3 6172 4809

PO Box 73
Bentleigh, VIC 3024

darrow@ormel.example

www.ormel.example

```html
<!DOCTYPE html>
<html lang="en">
<head>
<meta charset="utf-8">
<title>Ormel Property Development – Business Card</title>
<link href="https://fonts.googleapis.com/css2?family=Arimo:wght@400;700&display=swap" rel="stylesheet">
<style>
  :root {
    --backdrop: #2a2a2c;
    --steel-light: #8d8d8f;
    --steel-mid: #6c6c6e;
    --steel-dark: #4a4a4c;
    --ink: #f2f2f2;
    --ink-soft: #dcdcdc;
  }
  * { margin: 0; padding: 0; box-sizing: border-box; }
  html, body { width: 1200px; height: 720px; overflow: hidden; }
  body {
    background: var(--backdrop);
    display: flex;
    align-items: center;
    justify-content: center;
    font-family: "Arimo", Helvetica, Arial, sans-serif;
  }
  .business-card {
    position: relative;
    width: 900px;
    height: 520px;
    border-radius: 6px;
    background:
      linear-gradient(135deg, rgba(255,255,255,0) 30%, rgba(255,255,255,0.18) 55%, rgba(255,255,255,0) 75%),
      linear-gradient(180deg, var(--steel-light) 0%, var(--steel-mid) 55%, var(--steel-dark) 100%);
    box-shadow: 0 20px 50px rgba(0,0,0,0.55);
  }
  .brand {
    position: absolute;
    left: 70px;
    bottom: 90px;
    display: flex;
    align-items: center;
    gap: 18px;
    color: var(--ink);
    font-weight: 700;
  }
  .brand-square {
    width: 54px;
    height: 54px;
    background: var(--ink);
  }
  .brand-name {
    font-size: 30px;
    line-height: 1.15;
    letter-spacing: 0.5px;
  }
  .details {
    position: absolute;
    right: 60px;
    top: 90px;
    text-align: right;
    color: var(--ink);
  }
  .person-name {
    font-size: 34px;
    font-weight: 700;
  }
  .person-role {
    font-size: 20px;
    color: var(--ink-soft);
    margin-top: 2px;
  }
  .contact-list {
    list-style: none;
    margin-top: 42px;
  }
  .contact-item {
    display: flex;
    justify-content: flex-end;
    align-items: center;
    gap: 10px;
    font-size: 20px;
    line-height: 32px;
  }
  .contact-item svg { width: 18px; height: 18px; fill: var(--ink); }
  .postal-address {
    margin-top: 38px;
    font-size: 20px;
    padding-right: 28px;
  }
</style>
</head>
<body>
  <section class="business-card" aria-label="Ormel Property Development business card">
    <div class="brand">
      <span class="brand-square" aria-hidden="true"></span>
      <span class="brand-name">Ormel<br>Property Development</span>
    </div>

    <div class="details">
      <p class="person-name">Darrow Pketts</p>
      <p class="person-role">Managing Director</p>

      <ul class="contact-list">
        <li class="contact-item">+61 487 263 518
          <svg viewBox="0 0 18 18" aria-hidden="true"><path d="M5 1h8a1 1 0 0 1 1 1v14a1 1 0 0 1-1 1H5a1 1 0 0 1-1-1V2a1 1 0 0 1 1-1zm1 2v10h6V3z"/></svg>
        </li>
        <li class="contact-item">+61 3 6172 4809
          <svg viewBox="0 0 18 18" aria-hidden="true"><path d="M2 6c2-3 12-3 14 0l-1 2-3-1V5H6v2L3 8zM4 10h10v6H4z"/></svg>
        </li>
        <li class="contact-item">darrow@ormel.example
          <svg viewBox="0 0 18 18" aria-hidden="true"><path d="M1 4h16v10H1zm1.5 1.2L9 10l6.5-4.8V5h-13z"/></svg>
        </li>
        <li class="contact-item">www.ormel.example
          <svg viewBox="0 0 18 18" aria-hidden="true"><circle cx="9" cy="9" r="7.5" fill="none" stroke="#f2f2f2" stroke-width="1.5"/><path d="M1.5 9h15M9 1.5c-4 4-4 11 0 15M9 1.5c4 4 4 11 0 15" fill="none" stroke="#f2f2f2" stroke-width="1.2"/></svg>
        </li>
        <li class="contact-item">PO BOX 73 Bentleigh, VIC 3024
          <svg viewBox="0 0 18 18" aria-hidden="true"><path d="M9 2l8 7h-2v7h-4v-5H7v5H3V9H1z"/></svg>
        </li>
      </ul>
    </div>
  </section>
</body>
</html>
```